PixelGuild CEO Needs a Graphic for a Blog About Crowdsourcing and Online Employment

We need a simple graphic / banner for a blog post that's going to be posted on a large publication (like ByteHerald, Marlowe Commerce Quarterly).

The article will be written by Bram Ostiver (PixelGuild's CEO) and the title will be "Why Websites Will Become the Biggest Employers in the World". The article is about why online employers (like PixelGuild and Tasklynx) will one day have more 'workers' than offline employers.

We'd really like to get this ASAP - so early submissions encouraged. We will try and get the winning designer linked to from the article.

Note that this brief is similar to a previous project that we ran http://jobs.pixelguild-example.com/job.aspx?id=58213 where the article and design was published on ByteHerald http://byteherald-example.com/2012/12/08/asias-hidden-gig-surge/ and the designer (Moravia) was linked to from ByteHerald.

Target Market(s)

Entrepreneurs, journalists, small business owners, tech people.

Industry/Entity Type

Business

Requirements
Must have
• The graphic SHOULD have:
1) Have the text "Why Websites Will Become the Biggest Employers in the World" with some nice design and fonts (consider grey subtle pattern background and white drop shadow on fonts) - see attached examples
2) Have the dimensions 640px wide by 240px wide
Nice to have
• The graphic COULD have:

1) Incorporate the following words in the background (like a word cloud): crowdsource, microtask, crowdfund, witkey, outsource, freelance, online, work from home

OR

2) Incorporate logos of new online employers (Tasklynx, vYard, PixelGuild, ChoreFinch, Lunqiaofu, ClockworkPawn, Frameharbor) into the design. If the background of the graphic is grey, ideally, these logos would also be greyscale i.e. they should form a background motif.

OR

3) Show some graphic communicating themes from the article e.g. laptop, globe, workers, connections across the globe

OR

4) Have a second line of text "Why Crowdsourcing Websites Will Overtake Traditional Employers"
Should not have
• Should NOT have:
1) Any photos or clipart

```html
<!DOCTYPE html>
<html lang="en">
<head>
<meta charset="utf-8">
<title>Why Websites Will Become the Biggest Employers in the World</title>
<link rel="stylesheet" href="https://fonts.googleapis.com/css2?family=Oswald:wght@500;700&display=swap">
<style>
  :root {
    --paper: #ededed;
    --paper-light: #f6f6f6;
    --ink: #5a5a5a;
    --ink-strong: #3b3b3b;
    --accent: #1f74bd;
    --disc: #6f6f6f;
    --disc-dark: #4a4a4a;
    --rim: #ffffff;
    --glow: rgba(255, 255, 255, 0.9);
  }
  html, body {
    margin: 0;
    padding: 0;
    width: 1200px;
    height: 450px;
    overflow: hidden;
  }
  .banner {
    position: relative;
    width: 1200px;
    height: 450px;
    overflow: hidden;
    background: radial-gradient(ellipse at 35% 45%, var(--paper-light) 0%, var(--paper) 70%, #e2e2e2 100%);
    font-family: "Oswald", "Arial Narrow", sans-serif;
  }
  .headline {
    position: absolute;
    left: 0;
    top: 0;
    width: 760px;
    height: 450px;
  }
  .headline text {
    font-family: "Oswald", "Arial Narrow", sans-serif;
    font-weight: 700;
    text-transform: uppercase;
    fill: var(--ink);
    text-shadow: 1px 2px 0 var(--glow);
  }
  .headline .strong { fill: var(--ink-strong); }
  .headline .accent { fill: var(--accent); }
  .headline .subtitle {
    font-weight: 500;
    fill: var(--ink-strong);
  }
  .globe-frame {
    position: absolute;
    left: 735px;
    top: -35px;
    width: 520px;
    height: 520px;
    border-radius: 50%;
    background: var(--rim);
    box-shadow: -4px 4px 14px rgba(0, 0, 0, 0.25);
  }
  .globe-disc {
    position: absolute;
    left: 12px;
    top: 12px;
    width: 496px;
    height: 496px;
    border-radius: 50%;
    background: radial-gradient(circle at 40% 45%, var(--disc) 0%, var(--disc-dark) 100%);
  }
  .globe-network {
    position: absolute;
    left: 30px;
    top: 30px;
    width: 436px;
    height: 436px;
    border-radius: 50%;
    background: radial-gradient(circle at 38% 35%, #d9d9d9 0%, #9a9a9a 55%, #5c5c5c 100%);
  }
</style>
</head>
<body>
  <div class="banner">
    <svg class="headline" viewBox="0 0 760 450" role="heading" aria-level="1">
      <text x="22" y="109" font-size="58" textLength="696" lengthAdjust="spacingAndGlyphs">Why <tspan class="strong">Websites</tspan> will become the</text>
      <text class="strong" x="22" y="210" font-size="100" textLength="694" lengthAdjust="spacingAndGlyphs">Biggest Employers</text>
      <text x="150" y="296" font-size="58" textLength="150" lengthAdjust="spacingAndGlyphs">In the</text>
      <text class="accent" x="318" y="296" font-size="86" textLength="142" lengthAdjust="spacingAndGlyphs">World</text>
      <text class="subtitle" x="202" y="345" font-size="30" textLength="458" lengthAdjust="spacingAndGlyphs">Why crowdsourcing websites will</text>
      <text class="subtitle" x="202" y="392" font-size="30" textLength="410" lengthAdjust="spacingAndGlyphs">overtake traditional employers</text>
    </svg>
    <div class="globe-frame">
      <div class="globe-disc">
        <div class="globe-network" role="img" aria-label="Grey wireframe globe of curved bands linking oval nodes, showing online work connections around the world"></div>
      </div>
    </div>
  </div>
</body>
</html>
```